Business card design for IT consulting company

Looking for a simple, modern, clean business card design.
Open to reworking our existing logo.

Attached is our current business cards which we do not like.
Ideally double sided with something simple on the back.
Rectangle / Horizonal only.
No rounded edges on the card.
White as the dominate color is preferred.

Target Market(s)

clients, legal, oil & gas, medical, professionals

Industry/Entity Type

IT, tech, consulting

Contact Information for Business Card

Name, Title, email, phone, cell, website

Font styles to use
Sans Serif

Requirements
Must have
• Clean design
Should not have
• loud colors or unusual fonts, etc

```html
<!DOCTYPE html>
<html lang="en">
<head>
<meta charset="utf-8">
<title>Quilvane Solutions – Business Card</title>
<link href="https://fonts.googleapis.com/css2?family=Poppins:wght@400;500;600;700&display=swap" rel="stylesheet">
<style>
  :root{
    --stage:#ebebea;
    --card:#262626;
    --ink:#ffffff;
    --muted:#d6d6d6;
    --yellow:#f6c131;
    --blue:#3ea8de;
    --red:#e7434f;
    --navy:#27256f;
  }
  *{box-sizing:border-box;margin:0;padding:0}
  html,body{width:1200px;height:802px;overflow:hidden}
  body{background:var(--stage);font-family:'Poppins',sans-serif;position:relative}
  .card{position:absolute;top:252px;width:525px;height:300px;background:var(--card);box-shadow:0 10px 24px rgba(0,0,0,.22);overflow:hidden}
  .card--front{left:50px}
  .card--back{left:625px}

  .brand{position:absolute;display:flex;align-items:center;gap:12px;color:var(--ink);font-weight:600;letter-spacing:.3px;white-space:nowrap;line-height:1}
  .brand__square{display:block;flex:none;background:var(--blue)}
  .card--front .brand{right:40px;top:52px;font-size:32px}
  .card--front .brand__square{width:40px;height:40px}

  .identity{position:absolute;left:40px;top:146px}
  .identity__name{color:var(--blue);font-weight:700;font-size:21px;letter-spacing:.5px;line-height:1.1}
  .identity__title{color:var(--ink);font-size:14px;line-height:1.4}

  .rule{position:absolute;left:40px;right:40px;top:200px;height:3px;display:flex}
  .rule span{flex:1}
  .rule .y{background:var(--yellow)}
  .rule .b{background:var(--blue)}
  .rule .r{background:var(--red)}
  .rule .n{background:var(--navy)}

  .contacts{position:absolute;top:216px;list-style:none;color:var(--muted);font-size:14px;line-height:1.75}
  .contacts--phones{left:40px}
  .contacts--web{right:40px}
  .contacts li{display:flex;align-items:center;gap:8px}
  .contacts svg{width:13px;height:13px;flex:none}

  .card--back .brand{left:50%;top:50%;transform:translate(-50%,-50%);font-size:38px;gap:14px}
  .card--back .brand__square{width:50px;height:50px}
</style>
</head>
<body>
  <section class="card card--front" aria-label="Business card front">
    <div class="brand"><span class="brand__square"></span>Quilvane</div>

    <div class="identity">
      <p class="identity__name">DANIEL REYES</p>
      <p class="identity__title">IT Consultant</p>
    </div>

    <div class="rule"><span class="y"></span><span class="b"></span><span class="r"></span><span class="n"></span></div>

    <ul class="contacts contacts--phones">
      <li>
        <svg viewBox="0 0 16 16" fill="none" stroke="var(--blue)" stroke-width="1.6"><path d="M3 2h3l1.5 3.5-2 1.3a8 8 0 0 0 3.7 3.7l1.3-2L14 10v3a1 1 0 0 1-1 1A11 11 0 0 1 2 3a1 1 0 0 1 1-1z"/></svg>
        (888) 555-0147
      </li>
      <li>
        <svg viewBox="0 0 16 16" fill="none" stroke="var(--blue)" stroke-width="1.6"><rect x="4" y="1.5" width="8" height="13" rx="1.5"/><line x1="7" y1="12" x2="9" y2="12"/></svg>
        (604) 555-0193
      </li>
    </ul>

    <ul class="contacts contacts--web">
      <li>
        <svg viewBox="0 0 16 16" fill="none" stroke="var(--blue)" stroke-width="1.6"><rect x="1.5" y="3.5" width="13" height="9"/><path d="M1.5 3.5l6.5 5 6.5-5"/></svg>
        daniel.reyes@quilvane.ca
      </li>
      <li>
        <svg viewBox="0 0 16 16" fill="none" stroke="var(--blue)" stroke-width="1.4"><circle cx="8" cy="8" r="6.5"/><ellipse cx="8" cy="8" rx="3" ry="6.5"/><line x1="1.5" y1="8" x2="14.5" y2="8"/></svg>
        www.quilvane.ca
      </li>
    </ul>
  </section>

  <section class="card card--back" aria-label="Business card back">
    <div class="brand"><span class="brand__square"></span>Quilvane Solutions</div>
  </section>
</body>
</html>
```